Home Page Design for Motor Manufacturer

Hello,
please design the homepage for a manufacturer of industry motors. I am looking for a professional, clean and minimalistic design. Since this a rather conservative industry it should get a professional look but since it is a redesign there should be some modern that gives is the modern touch of innovation.
A competitor's homepage I like is:
https://www.valtrosk.com/en/
What I like about this website:
* clean, minimal, well structured design
* mega menu
For this project please find attached the wireframes (most buttons are in German but by context and Google translate you will easily figure it out; only unclear - "Messe" means "trade exhibition"). The paddings and margins are NOT exact. Also any color of backgrounds etc. chosen is not meant to represent a real color but rather to illustrate the object and maybe show there should be some background emphasis (color or image).
Wireframes:
https: //www.filmavek. com / t / pxuTQmD7ZJHaLrwY
In both wireframes the only thing that is different is the Service section. I expect from the winner both designs for this service section: one with normal cart design and one with tabs as filters to search products (find image for product categories attached)
In the header use on the left the following text:
h1: "Your competent partner for industrial engines,
-transmission and drawing parts
with more than 5000 satisfied customers "
primary button: Our products
sec. button: Download catalog
and on the right side we feature one or more product images (like putting them in a nice display together).
I also think of a solid background color or subtle gradient for the hero section.
The winner should also design an open mega menu version.
Menu items in this order:
• Home page
• Gearboxes & Motors
• Engine components
• Drawing parts
• Machines & accessories
• About us
• Contact
Also create a language switch with globe symbol and DE for Germany and EN for English above the nav plus the telephone number with icon (user dummy number +49 (0) 987654321)
Output should be in Figma, Sketch or PSD.
Fonts + color to use:
header: Proza Libre, bold, # 0171A1
body: Open Sans, regular, black
Primary accent color: # 0171A1
Text black or dark gray
background: light gray, white or shade of blue
More image resources:
https://www.filmavek.com/t/QrnLVdHZPKEX1bmu
If there are any questions please do not hesitate to ask.
Target Market(s)
B2B - anyone with industrial machinery needing small motors (not car engines)
Industry/Entity Type
Manufacturing
Number of Pages Required
1 page
Requirements
Must have
- see above
Nice to have
- see above
Should not have
- see above

```html
<!DOCTYPE html>
<html lang="en">
<head>
<meta charset="utf-8">
<title>Kelvar – Home</title>
<link rel="stylesheet" href="https://fonts.googleapis.com/css2?family=Open+Sans:ital,wght@0,400;0,600;1,400&family=Roboto:wght@400;500;700&family=Poppins:wght@500;700&display=swap">
<style>
:root{
  --accent:#0171a1;
  --ink:#222;
  --body:#444;
  --line:#e3ebf3;
  --tile:#eef3fb;
  --band:#4a4a4a;
  --white:#fff;
}
*{box-sizing:border-box;margin:0;padding:0}
html,body{width:684px;height:1200px;overflow:hidden;background:var(--white)}
body{position:relative;font-family:"Open Sans",sans-serif;color:var(--ink)}
.abs{position:absolute}

.topbar{left:0;top:0;width:684px;height:20px;background:var(--accent);color:var(--white);font-size:6.5px}
.topbar .item{position:absolute;top:5px;display:flex;align-items:center;gap:3px}
.switch{display:inline-block;width:14px;height:7px;border-radius:4px;background:#dfe8ef;position:relative;margin:0 2px}
.switch::after{content:"";position:absolute;left:1px;top:1px;width:5px;height:5px;border-radius:50%;background:#8fa3b2}
.social{position:absolute;top:6px;width:7px;height:7px;border-radius:50%;border:1px solid #bcd8e6}

.nav{left:0;top:20px;width:684px;height:48px;background:var(--white)}
.brand{position:absolute;left:60px;top:15px;font-family:"Roboto",sans-serif;font-weight:700;font-size:15px;color:var(--accent);letter-spacing:.5px}
.menu a{position:absolute;top:19px;font-weight:600;font-size:7.6px;color:#1f1f1f;text-decoration:none;white-space:nowrap}
.menu a.active{color:var(--accent)}
.menu a.active::after{content:"";position:absolute;left:-2px;right:-2px;bottom:-5px;height:1px;background:var(--accent)}

.hero{left:0;top:68px;width:684px;height:182px;overflow:hidden}
.hero-backdrop{position:absolute;inset:0;background:linear-gradient(90deg,#a9cfde 0%,#c3dbe6 40%,#d9e6ee 70%,#cfd9e0 100%)}
.product-display{position:absolute;left:312px;top:-20px;width:264px;height:230px;border-radius:50%;background:radial-gradient(circle at 50% 50%,#c9d3da 0%,#d8e0e6 30%,#e2e8ec 55%,rgba(226,232,236,0) 72%)}
.product-display.side{left:606px;top:0;width:110px;height:182px;border-radius:40% 0 0 40%;background:linear-gradient(90deg,rgba(200,206,212,0) 0%,#c3c8cd 40%,#d4d8dc 100%)}
.product-display.left{left:118px;top:0;width:80px;height:182px;border-radius:0;transform:skewX(-22deg);background:linear-gradient(90deg,rgba(160,175,185,0) 0%,rgba(150,160,170,.45) 50%,rgba(160,175,185,0) 100%)}
.hero h1{position:absolute;left:60px;top:40px;font-family:"Poppins",sans-serif;font-weight:700;font-size:24px;color:#1c1c1c;letter-spacing:-.2px}
.hero h1 span{color:var(--accent)}
.hero p{position:absolute;left:60px;top:74px;font-family:"Roboto",sans-serif;font-size:11.6px;line-height:14.6px;color:#444}
.btn{position:absolute;left:60px;top:118px;width:79px;height:21px;background:var(--accent);color:var(--white);font-family:"Roboto",sans-serif;font-weight:700;font-size:6.8px;letter-spacing:.6px;display:flex;align-items:center;justify-content:center}
.secondary{position:absolute;left:152px;top:121px;display:flex;align-items:center;gap:5px;font-family:"Roboto",sans-serif;font-size:8.4px;color:#222}

.card{position:absolute;top:280px;width:130px;height:126px;background:var(--white);border-radius:3px;box-shadow:0 0 10px rgba(0,40,80,.07);padding:16px 15px}
.card.featured{background:var(--accent);color:var(--white)}
.card svg{display:block;margin-bottom:11px}
.card h3{font-family:"Roboto",sans-serif;font-weight:700;font-size:9px;margin-bottom:9px}
.card p{font-size:7.4px;line-height:14px;color:#444}
.card.featured p{color:var(--white)}

.pill{left:291px;top:426px;width:102px;height:16px;border-radius:8px;background:#e4eef8;color:var(--accent);font-family:"Roboto",sans-serif;font-weight:700;font-size:6px;letter-spacing:.6px;display:flex;align-items:center;justify-content:center}
.section-title{left:0;top:449px;width:684px;text-align:center;font-family:"Roboto",sans-serif;font-weight:700;font-size:16.5px;color:#333}
.section-title span{color:var(--accent)}
.section-sub{left:200px;top:477px;width:284px;text-align:center;font-size:8.2px;font-weight:600;line-height:12.4px;color:#333}

.product{position:absolute;width:275px;background:var(--white);border:1px solid var(--line);text-align:center}
.product .photo{position:absolute;left:72px;width:128px;height:128px;background:radial-gradient(circle at 50% 50%,#c9ced4 0%,#dfe4ea 35%,var(--tile) 65%);border:1px solid #e1e8f2}
.product h4{position:absolute;left:0;width:100%;font-family:"Roboto",sans-serif;font-weight:700;font-size:12px;color:#222}
.product p{position:absolute;left:14px;width:247px;font-size:7.2px;line-height:12.2px;color:#444}

.testimonial{left:0;top:1030px;width:684px;height:170px;background:var(--band);color:var(--white);text-align:center}
.avatar{position:absolute;left:317px;top:18px;width:50px;height:50px;border-radius:50%;background:linear-gradient(160deg,#e6e8eb,#8c8f94);border:3px solid #6a6a6a}
.testimonial h5{position:absolute;left:0;top:73px;width:100%;font-family:"Roboto",sans-serif;font-weight:700;font-size:10px}
.testimonial .role{position:absolute;left:0;top:88px;width:100%;font-family:"Roboto",sans-serif;font-size:6.8px;color:#ddd}
.testimonial blockquote{position:absolute;left:115px;top:104px;width:454px;font-style:italic;font-size:8.4px;line-height:15px;color:#eee}
.dots{position:absolute;left:317px;top:148px;display:flex;gap:6px}
.dots i{width:5px;height:5px;border-radius:50%;background:#aaa}
.dots i.on{background:var(--accent)}
</style>
</head>
<body>

<header class="abs topbar">
  <div class="item" style="left:60px">
    <svg width="6" height="5" viewBox="0 0 6 5"><rect width="6" height="5" fill="#fff"/><path d="M0 0l3 2.5L6 0" stroke="#0171a1" stroke-width=".7" fill="none"/></svg>
    contact@example.com
  </div>
  <div class="item" style="left:156px">
    <svg width="6" height="6" viewBox="0 0 24 24"><path fill="#fff" d="M6.6 10.8a15 15 0 006.6 6.6l2.2-2.2c.3-.3.7-.4 1-.2 1.1.4 2.3.6 3.6.6.6 0 1 .4 1 1V20c0 .6-.4 1-1 1A17 17 0 013 4c0-.6.4-1 1-1h3.5c.6 0 1 .4 1 1 0 1.3.2 2.5.6 3.6.1.3 0 .7-.2 1z"/></svg>
    +49 (0) 987654321
  </div>
  <div class="item" style="left:456px">
    <svg width="6" height="6" viewBox="0 0 10 10"><circle cx="5" cy="5" r="4.2" fill="none" stroke="#fff"/><path d="M1 5h8M5 1c2 2 2 6 0 8M5 1c-2 2-2 6 0 8" stroke="#fff" stroke-width=".7" fill="none"/></svg>
    Germany <span class="switch"></span> English
  </div>
  <span class="social" style="left:552px"></span>
  <span class="social" style="left:568px"></span>
  <span class="social" style="left:584px"></span>
  <span class="social" style="left:600px"></span>
  <span class="social" style="left:617px"></span>
</header>

<nav class="abs nav">
  <div class="brand">Kelvar</div>
  <div class="menu">
    <a class="active" style="left:146px">Home</a>
    <a style="left:185px">Gearboxes &amp; Motors</a>
    <a style="left:278px">Engine Components</a>
    <a style="left:369px">Drawing Parts</a>
    <a style="left:438px">Machines &amp; accessories
      <svg width="6" height="4" viewBox="0 0 6 4" style="margin-left:3px"><path d="M.5.5L3 3 5.5.5" stroke="#222" stroke-width="1" fill="none"/></svg></a>
    <a style="left:555px">About</a>
    <a style="left:594px">Contact</a>
  </div>
</nav>

<section class="abs hero">
  <div class="hero-backdrop"></div>
  <div class="product-display left" role="img" aria-label="Faded photo of a geared motor housing"></div>
  <div class="product-display" role="img" aria-label="Product display: photo of a harmonic gear reducer"></div>
  <div class="product-display side" role="img" aria-label="Product display: photo of a planetary gearbox"></div>
  <h1>Welcome to <span>Kelvar</span></h1>
  <p>Your competent partner for industrial engines,<br>-transmission and drawing parts with more than 5000 satisfied customers</p>
  <div class="btn">OUR PRODUCTS</div>
  <div class="secondary">
    <svg width="16" height="16" viewBox="0 0 16 16"><circle cx="8" cy="8" r="7" fill="none" stroke="#0171a1" stroke-width="1.3"/><path d="M8 4.3v5.4M5.6 7.5L8 9.9l2.4-2.4M5 11.6h6" stroke="#0171a1" stroke-width="1.3" fill="none"/></svg>
    Download catalog
  </div>
</section>

<article class="card featured" style="left:60px">
  <svg width="21" height="21" viewBox="0 0 24 24" fill="none" stroke="#fff" stroke-width="1.8"><circle cx="12" cy="12" r="10"/><path d="M2 12h20M12 2a14 14 0 010 20M5 5c4 2 8 9 9 17M19 5c-4 2-9 6-17 7"/></svg>
  <h3>Vorteil - 1</h3>
  <p>Voluptatum deleniti atque corrupti quos dolores et quas molestias excepturi</p>
</article>
<article class="card" style="left:205px">
  <svg width="21" height="21" viewBox="0 0 24 24" fill="none" stroke="#0171a1" stroke-width="1.8"><path d="M6 2h8l5 5v15H6z"/><path d="M14 2v5h5M9 12h7M9 15h7M9 18h7"/></svg>
  <h3>Vorteil - 2</h3>
  <p>Duis aute irure dolor in reprehenderit in voluptate velit esse cillum dolore</p>
</article>
<article class="card" style="left:350px">
  <svg width="21" height="21" viewBox="0 0 24 24" fill="none" stroke="#0171a1" stroke-width="2"><path d="M3 18a9 9 0 1118 0z"/><path d="M12 17l4-6"/></svg>
  <h3>Vorteil - 3</h3>
  <p>Excepteur sint occaecat cupidatat non proident, sunt in culpa qui officia</p>
</article>
<article class="card" style="left:495px">
  <svg width="21" height="21" viewBox="0 0 24 24"><circle cx="12" cy="12" r="10" fill="#0171a1"/><path d="M6 7c2 1 3 3 2 5s1 4 0 6M14 4c0 3 3 3 3 6s2 2 3 3" stroke="#fff" stroke-width="2" fill="none"/></svg>
  <h3>Vorteil - 4</h3>
  <p>At vero eos et accusamus et iusto odio dignissimos ducimus qui blanditiis</p>
</article>

<div class="abs pill">GEARBOXES &amp; MOTORS</div>
<h2 class="abs section-title">Check our <span>Gearboxes &amp; Motors</span></h2>
<p class="abs section-sub">Ut possimus qui ut temporibus culpa velit eveniet modi omnis est adipisci expedita at voluptas atque vitae autem.</p>

<div class="product" style="left:60px;top:517px;height:267px">
  <div class="photo" style="top:41px" role="img" aria-label="Photo of a harmonic gear reducer"></div>
  <h4 style="top:179px">Product Title</h4>
  <p style="top:201px">Product Details: Voluptatum deleniti atque corrupti quos dolores et quas molestias excepturi</p>
</div>
<div class="product" style="left:350px;top:517px;height:267px">
  <div class="photo" style="top:41px" role="img" aria-label="Photo of a planetary geared motor"></div>
  <h4 style="top:179px">Product Title</h4>
  <p style="top:201px">Product Details: Voluptatum deleniti atque corrupti quos dolores et quas molestias excepturi</p>
</div>
<div class="product" style="left:60px;top:783px;height:260px">
  <div class="photo" style="top:41px" role="img" aria-label="Photo of a right-angle planetary gearbox"></div>
  <h4 style="top:179px">Product Title</h4>
  <p style="top:201px">Product Details: Voluptatum deleniti atque corrupti quos dolores et quas molestias excepturi</p>
</div>
<div class="product" style="left:350px;top:795px;height:250px">
  <div class="photo" style="top:41px" role="img" aria-label="Photo of a long geared DC motor"></div>
  <h4 style="top:179px">Product Title</h4>
  <p style="top:201px">Product Details: Voluptatum deleniti atque corrupti quos dolores et quas molestias excepturi</p>
</div>

<section class="abs testimonial">
  <div class="avatar" role="img" aria-label="Portrait photo of the company founder"></div>
  <h5>Marten Feld</h5>
  <div class="role">Ceo &amp; Founder</div>
  <blockquote>“ Proin iaculis purus consequat sem cure digni ssim donec porttitora entum suscipit rhoncus. Accusantium quam, ultricies eget id, aliquam eget nibh et. Maecen aliquam, risus at semper. ”</blockquote>
  <div class="dots"><i class="on"></i><i></i><i></i><i></i><i></i></div>
</section>

</body>
</html>
```